Email Signature Block Design for Law Firm

I would like you to create a similar signature block for my law firm . I saw the email signature block attached as image002.png and wanted a similar design for my law firm. I want to be able to swap the portraits for each of my staff from the final design. Our law firm colors are black, gold, white, red.

Industry/Entity Type

Law

Requirements
Nice to have
• i like the red circle in around the photo in the 8 copper bench design. The 9 Copper Bench desgn is what inspired me to have a signature block design for my firm.

```html
<!DOCTYPE html>
<html lang="en">
<head>
<meta charset="utf-8">
<title>The Harlow Firm – Email Signature</title>
<link rel="stylesheet" href="https://fonts.googleapis.com/css2?family=Montserrat:wght@400;500&display=swap">
<style>
  :root {
    --page: #ffffff;
    --band: #000000;
    --gold: #e09a2a;
    --gold-line: #b8782a;
    --red: #c0262d;
    --text: #ffffff;
    --portrait-light: #ffffff;
    --portrait-dark: #1a1a1a;
  }
  * { margin: 0; padding: 0; box-sizing: border-box; }
  html, body {
    width: 1200px;
    height: 1000px;
    overflow: hidden;
    background: var(--page);
    font-family: "Montserrat", Arial, sans-serif;
  }
  .canvas { position: relative; width: 1200px; height: 1000px; }

  .signature {
    position: absolute;
    left: 29px; top: 305px;
    width: 1125px; height: 375px;
    background: var(--band);
    color: var(--text);
  }

  .firm-name {
    position: absolute;
    left: 33px; top: 44px;
    display: flex; align-items: center; gap: 14px;
    font-size: 19px; font-weight: 500;
    letter-spacing: 0.04em;
    color: var(--text);
  }
  .firm-name__dot {
    width: 22px; height: 22px; border-radius: 50%;
    background: var(--gold);
  }

  .person {
    position: absolute;
    left: 88px; top: 172px;
  }
  .person__name {
    font-size: 28px; font-weight: 500;
    letter-spacing: 0.02em;
    line-height: 1;
  }
  .person__role {
    margin-top: 10px;
    font-size: 19px; font-weight: 400;
  }

  .rule {
    position: absolute;
    top: 279px; height: 1.5px;
    background: var(--gold-line);
  }
  .rule--left { left: 25px; width: 399px; }
  .rule--right { left: 701px; width: 399px; }

  .portrait-frame {
    position: absolute;
    left: 406px; top: 31px;
    width: 314px; height: 314px;
    border-radius: 50%;
    border: 6px solid var(--gold);
    box-shadow: inset 0 0 0 3px var(--red);
    overflow: hidden;
    background: var(--portrait-light);
  }
  .portrait {
    width: 100%; height: 100%;
    border-radius: 50%;
    border: 3px solid var(--red);
    background: linear-gradient(180deg, var(--portrait-light) 0%, #e8e4e0 45%, var(--portrait-dark) 75%);
  }

  .contact {
    position: absolute;
    left: 806px; top: 162px;
    font-size: 18.5px; font-weight: 500;
    line-height: 33px;
    letter-spacing: 0.01em;
  }
</style>
</head>
<body>
  <div class="canvas">
    <section class="signature">
      <div class="firm-name">
        <span class="firm-name__dot"></span>
        <span>THE HARLOW FIRM, PLLC</span>
      </div>

      <div class="person">
        <p class="person__name">MARCUS HARLOW</p>
        <p class="person__role">Attorney</p>
      </div>

      <div class="rule rule--left"></div>
      <div class="rule rule--right"></div>

      <div class="portrait-frame">
        <div class="portrait" role="img" aria-label="Portrait photo of the attorney in a dark suit and blue striped tie on a white background"></div>
      </div>

      <div class="contact">
        <p class="contact__phone">555-014-2929</p>
        <p class="contact__web">WESEEKFAIRNESS.COM</p>
      </div>
    </section>
  </div>
</body>
</html>
```